Pinewharfs Vehicle Wrap Design for Vacation Rental Property Mgt Company

We are looking for a vehicle wrap design to extend our brand through our service vehicles. Design should be simple, professional, eye-catching, and incorporate our logo and corporate colors. Design should be flexible enough to be applied to a wide variety of trucks and cars. Not looking for FULL wrap, but rather separate graphics to be applied to white vehicles. Attached is ppt with a couple of our current vehicles and a few sample designs that has caught our attention. Copies of our current logo and biz card designs are also included.

Panels to include:
Logo (attached)
555-318-6249
www.Pinewharves.example
Vacation Rental Property Management
Property Maintenance Services
Linen & Laundry Services

Target Market(s)

Local adults 30-65

Industry/Entity Type

Font styles to use
Serif

Colors
0054AA
0677BA
7BADD7
CADEEF
E8F1F8

Requirements
Must have
• Logo, phone, web address, corporate colors,

```html
<!DOCTYPE html>
<html lang="en">
<head>
<meta charset="utf-8">
<title>Pinewharves Vehicle Wrap Graphics</title>
<link rel="stylesheet" href="https://fonts.googleapis.com/css2?family=Oswald:wght@500&family=Montserrat:wght@500;600&display=swap">
<style>
  :root {
    --navy: #34466f;
    --navy-deep: #24356a;
    --accent: #3a8fc8;
    --paper: #ffffff;
    --backdrop: #eef1f5;
    --edge: #d5dbe4;
  }
  * { margin: 0; padding: 0; box-sizing: border-box; }
  html, body { width: 1200px; height: 1200px; overflow: hidden; background: var(--backdrop); }
  .canvas { position: relative; width: 1200px; height: 1200px; }
  .artboard { position: absolute; background: var(--paper); border: 1px solid var(--edge); overflow: hidden; }
  .wordmark { font-family: "Oswald", sans-serif; font-weight: 500; color: var(--navy); letter-spacing: 1px; line-height: 1; white-space: nowrap; }
  .tagline { font-family: "Montserrat", sans-serif; font-weight: 600; color: var(--navy); letter-spacing: 2px; white-space: nowrap; }
  .brand-square { flex: none; background: var(--navy); }
  .phone, .web-caps { font-family: "Oswald", sans-serif; font-weight: 500; line-height: 1; white-space: nowrap; }
  .services { list-style: none; font-family: "Montserrat", sans-serif; font-weight: 500; color: var(--paper); }
  .services li { display: flex; align-items: flex-start; gap: 10px; white-space: nowrap; }
  .services svg { flex: none; margin-top: 4px; }

  /* side panel */
  .side { left: 40px; top: 50px; width: 1120px; height: 500px; }
  .side .slab { position: absolute; inset: 0; }
  .side .lockup { position: absolute; left: 50px; top: 165px; width: 620px; text-align: center; }
  .side .lockup-row { display: flex; align-items: center; justify-content: center; gap: 20px; }
  .side .brand-square { width: 62px; height: 62px; }
  .side .wordmark { font-size: 90px; }
  .side .tagline { font-size: 24px; margin-top: 18px; }
  .side .info { position: absolute; left: 775px; top: 110px; width: 330px; }
  .side .services { font-size: 17px; line-height: 1.45; }
  .side .phone { color: var(--paper); font-size: 52px; margin-top: 34px; }
  .side .web-caps { color: var(--paper); font-size: 23px; margin-top: 14px; letter-spacing: 1px; }

  /* front hood */
  .front { left: 40px; top: 600px; width: 520px; height: 260px; }
  .front .lockup { position: absolute; inset: 0; display: flex; flex-direction: column; align-items: center; justify-content: center; }
  .front .lockup-row { display: flex; align-items: center; gap: 14px; }
  .front .brand-square { width: 36px; height: 36px; }
  .front .wordmark { font-size: 56px; }
  .front .tagline { font-size: 14px; margin-top: 10px; }

  /* rear doors */
  .rear { left: 600px; top: 600px; width: 560px; height: 550px; }
  .rear .door-split { position: absolute; left: 279px; top: 0; width: 2px; height: 100%; background: var(--backdrop); }
  .rear .lockup { position: absolute; left: 30px; top: 70px; width: 500px; text-align: center; }
  .rear .lockup-row { display: flex; align-items: center; justify-content: center; gap: 16px; }
  .rear .brand-square { width: 44px; height: 44px; }
  .rear .wordmark { font-size: 62px; }
  .rear .tagline { font-size: 17px; margin-top: 12px; }
  .rear .web { font-family: "Montserrat", sans-serif; font-weight: 500; color: var(--navy); font-size: 17px; margin-top: 16px; white-space: nowrap; }
  .rear .phone { position: absolute; left: 30px; top: 280px; color: var(--navy); font-size: 48px; }
  .rear .band { position: absolute; left: 0; right: 0; top: 350px; bottom: 0; background: var(--navy-deep); }
  .rear .services { position: absolute; left: 296px; top: 400px; width: 255px; font-size: 12.5px; line-height: 1.45; }
  .rear .services li { gap: 8px; }
  .rear .services svg { margin-top: 2px; }
</style>
</head>
<body>
<main class="canvas">

  <section class="artboard side" aria-label="Side panel graphic">
    <svg class="slab" viewBox="0 0 1120 500" preserveAspectRatio="none" aria-hidden="true">
      <polygon points="790,0 1120,0 1120,500 640,500" fill="var(--navy)"/>
    </svg>
    <div class="lockup">
      <div class="lockup-row">
        <span class="brand-square"></span>
        <span class="wordmark">PINEWHARVES</span>
      </div>
      <p class="tagline">VACATION RENTALS</p>
    </div>
    <div class="info">
      <ul class="services">
        <li><svg width="16" height="16" viewBox="0 0 18 18"><path d="M2 10 L7 15 L16 3" fill="none" stroke="var(--accent)" stroke-width="3"/></svg><span>Vacation Rental<br>Property Management</span></li>
        <li><svg width="16" height="16" viewBox="0 0 18 18"><path d="M2 10 L7 15 L16 3" fill="none" stroke="var(--accent)" stroke-width="3"/></svg><span>Property Maintenance Services</span></li>
        <li><svg width="16" height="16" viewBox="0 0 18 18"><path d="M2 10 L7 15 L16 3" fill="none" stroke="var(--accent)" stroke-width="3"/></svg><span>Linen &amp; Laundry Services</span></li>
      </ul>
      <p class="phone">555-318-6249</p>
      <p class="web-caps">WWW.PINEWHARVES.EXAMPLE</p>
    </div>
  </section>

  <section class="artboard front" aria-label="Hood graphic">
    <div class="lockup">
      <div class="lockup-row">
        <span class="brand-square"></span>
        <span class="wordmark">PINEWHARVES</span>
      </div>
      <p class="tagline">VACATION RENTALS</p>
    </div>
  </section>

  <section class="artboard rear" aria-label="Rear doors graphic">
    <div class="band"></div>
    <div class="door-split"></div>
    <div class="lockup">
      <div class="lockup-row">
        <span class="brand-square"></span>
        <span class="wordmark">PINEWHARVES</span>
      </div>
      <p class="tagline">VACATION RENTALS</p>
      <p class="web">www.Pinewharves.example</p>
    </div>
    <p class="phone">555-318-6249</p>
    <ul class="services">
      <li><svg width="13" height="13" viewBox="0 0 18 18"><path d="M2 10 L7 15 L16 3" fill="none" stroke="var(--accent)" stroke-width="3"/></svg><span>Vacation Rental<br>Property Management</span></li>
      <li><svg width="13" height="13" viewBox="0 0 18 18"><path d="M2 10 L7 15 L16 3" fill="none" stroke="var(--accent)" stroke-width="3"/></svg><span>Property Maintenance Services</span></li>
      <li><svg width="13" height="13" viewBox="0 0 18 18"><path d="M2 10 L7 15 L16 3" fill="none" stroke="var(--accent)" stroke-width="3"/></svg><span>Linen &amp; Laundry Services</span></li>
    </ul>
  </section>

</main>
</body>
</html>
```